Postcard Design for Marketing to Builders

I am an architect that gets most of my work from contractor's. I design residential and commercial projects based in California. My main focus is California's Central Coast. I want the feel of the postcard to reflect a strong professional, efficient and creative partner for contractors (Builders). I have provide some photos of projects I have done recently to use on the postcard if needed. I have also included my logo which I would like on the front.

Industry/Entity Type

Architect

Font styles to use
Serif

```html
<!DOCTYPE html>
<html lang="en">
<head>
<meta charset="utf-8">
<title>Daniel R Whitford – Postcard</title>
<link href="https://fonts.googleapis.com/css2?family=Oswald:wght@500;700&family=Cinzel:wght@400;700&family=Lato:wght@400;700&display=swap" rel="stylesheet">
<style>
:root{
  --backdrop:#6e4a2c;
  --navy:#2a2f8a;
  --navy-deep:#1b1f63;
  --orange:#e8501f;
  --orange-dark:#b93a12;
  --ink:#1d1d1d;
  --paper:#ffffff;
  --mist:#eeeeee;
  --charcoal:#2a2a2a;
  --stamp:#a9a9ad;
}
*{margin:0;padding:0;box-sizing:border-box}
html,body{width:907px;height:1200px;overflow:hidden}
body{background:var(--backdrop);position:relative;font-family:'Lato',sans-serif;color:var(--ink)}
.card{position:absolute;left:67px;width:770px;background:var(--paper);overflow:hidden}
.card--front{top:78px;height:496px;background:linear-gradient(#fff 60%,#e9e9e9)}
.card--back{top:629px;height:497px}
.front-band{position:absolute;left:0;top:0;width:770px;height:332px;background:linear-gradient(100deg,var(--navy-deep),var(--navy) 55%,#3138a0)}
.house-frame{position:absolute;left:0;top:0}
.brand{position:absolute;right:30px;top:94px;width:150px;display:flex;align-items:center;justify-content:center;gap:6px;font-family:'Cinzel',serif;font-size:14px;color:#fff}
.brand__mark{width:8px;height:8px;background:#fff}
.headline{position:absolute;right:20px;top:146px;text-align:right}
.headline__lead{font-family:'Oswald',sans-serif;font-weight:700;font-size:30px;color:var(--orange);line-height:36px}
.headline__mid{font-family:'Oswald',sans-serif;font-weight:500;font-size:18px;color:#fff;line-height:26px}
.headline__tail{font-family:'Cinzel',serif;font-size:21px;color:#fff;line-height:30px;letter-spacing:.5px}
.ribbon{position:absolute;left:425px;top:274px}
.call{position:absolute;left:520px;top:284px;width:210px;text-align:center;color:#fff}
.call__label{font-family:'Oswald',sans-serif;font-weight:700;font-size:21px;line-height:28px}
.call__phone{font-family:'Cinzel',serif;font-size:20px;line-height:32px;display:flex;align-items:center;justify-content:center;gap:8px}
.about{position:absolute;left:35px;top:368px;width:362px}
.about__title{font-family:'Cinzel',serif;font-size:15px;color:var(--orange);line-height:18px}
.about__text{font-size:13px;line-height:17px;text-align:justify}
.contact{font-size:13.5px;line-height:18px}
.contact__row{display:flex;gap:7px;align-items:flex-start;margin-bottom:8px}
.contact__row svg{flex:none;margin-top:3px}
.contact--front{position:absolute;left:497px;top:390px}
.back-photo{position:absolute;left:0;top:0;width:374px;height:166px;background:linear-gradient(#8fb9e0,#cfd9e2 45%,#b9a98a 60%,#6f6f70 80%,#8a8a8a)}
.stripe-h{position:absolute;left:0;top:168px;width:376px;height:9px;background:var(--orange);border-bottom:3px solid var(--navy)}
.stripe-v{position:absolute;left:374px;top:0;width:16px;height:497px;background:linear-gradient(90deg,var(--orange) 0 5px,#fff 5px 8px,var(--navy) 8px 12px,#fff 12px)}
.services{position:absolute;left:0;top:192px;width:374px}
.services__title{font-family:'Cinzel',serif;font-size:17px;color:var(--orange);text-align:center;letter-spacing:.5px}
.services__cols{display:flex;margin-top:6px}
.services__list{list-style:none;font-size:12.5px;line-height:18.6px}
.services__list:first-child{margin-left:39px;width:169px}
.services__list li{display:flex;align-items:center;gap:5px}
.contact-panel{position:absolute;left:0;top:398px;width:207px;height:99px;background:var(--charcoal);color:#fff;padding:18px 0 0 28px}
.contact--back{font-size:10px;line-height:12px}
.contact--back .contact__row{margin-bottom:7px}
.map{position:absolute;left:207px;top:361px;width:167px;height:136px;border:4px solid var(--orange);border-right:none;border-bottom:none;border-radius:6px 0 0 0;background:linear-gradient(135deg,#eceae4,#dcdad3)}
.address-side{position:absolute;left:390px;top:0;width:380px;height:497px}
.faint-photo{position:absolute;left:0;top:140px;width:380px;height:357px;background:linear-gradient(#f4f4f4,#e3e3e3 60%,#ececec)}
.stamp{position:absolute;right:7px;top:19px;width:56px;height:63px;background:var(--stamp)}
.brand--back{position:absolute;left:0;top:455px;width:150px;display:flex;align-items:center;justify-content:center;gap:6px;font-family:'Cinzel',serif;font-size:13px;color:var(--navy)}
.brand--back .brand__mark{background:var(--navy)}
</style>
</head>
<body>

<section class="card card--front">
  <div class="front-band"></div>
  <svg class="house-frame" width="440" height="332" viewBox="0 0 440 332">
    <defs>
      <linearGradient id="buildingTones" x1="0" y1="0" x2="0" y2="1">
        <stop offset="0" stop-color="#7fb2e6"/>
        <stop offset=".35" stop-color="#c9ae86"/>
        <stop offset=".7" stop-color="#8a7a5e"/>
        <stop offset="1" stop-color="#5e7a3e"/>
      </linearGradient>
    </defs>
    <path role="img" aria-label="Photo of a three-story office building with landscaping"
      d="M8 137 L81 80 L81 22 L113 22 L113 55 L186 4 L433 137 L381 137 L381 320 L43 320 L43 137 Z"
      fill="url(#buildingTones)" stroke="#fff" stroke-width="6" stroke-linejoin="miter"/>
  </svg>

  <div class="brand"><span class="brand__mark"></span>Daniel R Whitford</div>

  <div class="headline">
    <div class="headline__lead">DESIGN RESIDENTIAL</div>
    <div class="headline__mid">AND COMMERCIAL PROJECTS</div>
    <div class="headline__tail">BASED IN CALIFORNIA</div>
  </div>

  <svg class="ribbon" width="345" height="95" viewBox="0 0 345 95">
    <polygon points="0,41 96,41 96,95" fill="var(--orange-dark)"/>
    <rect x="28" y="0" width="317" height="66" fill="var(--orange)"/>
    <polygon points="0,41 28,0 28,66" fill="var(--orange)"/>
  </svg>
  <div class="call">
    <div class="call__label">CALL NOW</div>
    <div class="call__phone">
      <svg width="18" height="18" viewBox="0 0 18 18"><circle cx="9" cy="9" r="8" fill="none" stroke="var(--navy-deep)" stroke-width="1.5"/><path d="M6 5c-1 2 1 6 4 8l1.5-1.5-1.5-1.5-1 .5c-1-1-1.5-2-1.5-3l1-.5L8 5z" fill="var(--navy-deep)"/></svg>
      (209) 555-0147
    </div>
  </div>

  <div class="about">
    <h2 class="about__title">ABOUT DANIEL WHITFORD</h2>
    <p class="about__text">A licensed architect for almost 25 years. He has designed everything from a patio cover to a 3-story office building and everything else in between. He has worked with hundreds of clients and has learned how to help clients complete their vision for their project.</p>
  </div>

  <div class="contact contact--front">
    <div class="contact__row">
      <svg width="12" height="11" viewBox="0 0 12 11"><path d="M6 0L0 5h2v6h3V8h2v3h3V5h2z" fill="var(--orange)"/></svg>
      <span>PO Box 2210, Harbor Ridge<br>CA 93499</span>
    </div>
    <div class="contact__row">
      <svg width="9" height="9" viewBox="0 0 9 9"><circle cx="4.5" cy="4.5" r="4.5" fill="var(--orange)"/></svg>
      <span>www.CoastlineDraftingStudio.com</span>
    </div>
  </div>
</section>

<section class="card card--back">
  <div class="back-photo" role="img" aria-label="Photo of a single-story clinic building with a parking lot"></div>
  <div class="stripe-h"></div>

  <div class="services">
    <h2 class="services__title">MY SERVICES</h2>
    <div class="services__cols">
      <ul class="services__list">
        <li><svg width="8" height="8" viewBox="0 0 8 8"><path d="M0 4l3 3 5-6" fill="none" stroke="var(--orange)" stroke-width="1.8"/></svg>Adelaide</li>
        <li><svg width="8" height="8" viewBox="0 0 8 8"><path d="M0 4l3 3 5-6" fill="none" stroke="var(--orange)" stroke-width="1.8"/></svg>Arroyo Grande</li>
        <li><svg width="8" height="8" viewBox="0 0 8 8"><path d="M0 4l3 3 5-6" fill="none" stroke="var(--orange)" stroke-width="1.8"/></svg>Atascadero</li>
        <li><svg width="8" height="8" viewBox="0 0 8 8"><path d="M0 4l3 3 5-6" fill="none" stroke="var(--orange)" stroke-width="1.8"/></svg>Avila Beach</li>
        <li><svg width="8" height="8" viewBox="0 0 8 8"><path d="M0 4l3 3 5-6" fill="none" stroke="var(--orange)" stroke-width="1.8"/></svg>Baywood Park</li>
        <li><svg width="8" height="8" viewBox="0 0 8 8"><path d="M0 4l3 3 5-6" fill="none" stroke="var(--orange)" stroke-width="1.8"/></svg>California Valley</li>
        <li><svg width="8" height="8" viewBox="0 0 8 8"><path d="M0 4l3 3 5-6" fill="none" stroke="var(--orange)" stroke-width="1.8"/></svg>Cambria</li>
      </ul>
      <ul class="services__list">
        <li><svg width="8" height="8" viewBox="0 0 8 8"><path d="M0 4l3 3 5-6" fill="none" stroke="var(--orange)" stroke-width="1.8"/></svg>Camp Roberts</li>
        <li><svg width="8" height="8" viewBox="0 0 8 8"><path d="M0 4l3 3 5-6" fill="none" stroke="var(--orange)" stroke-width="1.8"/></svg>Casmalia</li>
        <li><svg width="8" height="8" viewBox="0 0 8 8"><path d="M0 4l3 3 5-6" fill="none" stroke="var(--orange)" stroke-width="1.8"/></svg>Cayucos</li>
        <li><svg width="8" height="8" viewBox="0 0 8 8"><path d="M0 4l3 3 5-6" fill="none" stroke="var(--orange)" stroke-width="1.8"/></svg>Cholame</li>
        <li><svg width="8" height="8" viewBox="0 0 8 8"><path d="M0 4l3 3 5-6" fill="none" stroke="var(--orange)" stroke-width="1.8"/></svg>Creston</li>
        <li><svg width="8" height="8" viewBox="0 0 8 8"><path d="M0 4l3 3 5-6" fill="none" stroke="var(--orange)" stroke-width="1.8"/></svg>Grover Beach</li>
        <li><svg width="8" height="8" viewBox="0 0 8 8"><path d="M0 4l3 3 5-6" fill="none" stroke="var(--orange)" stroke-width="1.8"/></svg>Guadalupe</li>
      </ul>
    </div>
  </div>

  <div class="contact-panel">
    <div class="contact contact--back">
      <div class="contact__row">
        <svg width="9" height="8" viewBox="0 0 12 11"><path d="M6 0L0 5h2v6h3V8h2v3h3V5h2z" fill="var(--orange)"/></svg>
        <span>PO Box 2210, Harbor<br>Ridge CA 93499</span>
      </div>
      <div class="contact__row">
        <svg width="8" height="8" viewBox="0 0 9 9"><circle cx="4.5" cy="4.5" r="4.5" fill="var(--orange)"/></svg>
        <span>(209) 555-0147</span>
      </div>
      <div class="contact__row">
        <svg width="8" height="8" viewBox="0 0 9 9"><circle cx="4.5" cy="4.5" r="4.5" fill="var(--orange)"/></svg>
        <span>www.CoastlineDraftingStudio.com</span>
      </div>
    </div>
  </div>

  <div class="map" role="img" aria-label="Street map showing the office location"></div>
  <div class="stripe-v"></div>

  <div class="address-side">
    <div class="faint-photo" role="img" aria-label="Faded photo of the clinic building entrance"></div>
    <div class="stamp"></div>
    <div class="brand brand--back"><span class="brand__mark"></span>Daniel R Whitford</div>
  </div>
</section>

</body>
</html>
```